Flyer for an online formula one racing league

Hello.

I am looking for the perfect one page facebook/instagram style flyer for an online formula one racing league. The racing league is called 'VOLTA RACING LEAGUE'.

Information that MUST be on the new flyer is already on the old flyer I have uploaded here. In addition to including: The Volta racing league 'V' logo I have uploaded AND the text: 'Very popular, clean and competitive racing league, running for its 4th season. Why not join with a friend? Race times, Mondays, Tuesdays and Wednesdays each at 8pm UK TIME Message below for any questions. (Spacing of information is not important, however all the information in regards to the racing I have just mentioned MUST BE on the flyer, this includes info from old pic, logo and the other info I just mentioned).

It would be beneficial to have lots of dark blue on the flyer and the new flyer to be a lot different to the original flyer I uploaded, but this is not essential.

I apologise if I did not explain very well, any questions, please message me.

The best flyer should look the most attractive to someone that might be interested in joining an online formula one racing league.

I used this website before to create the perfect logo for my Sunday League team last year, and I was very impressed. I look forward to seeing your submissions.

Target Market(s)

No specific target, more something that may attract someone into joining a formula one online racing league

Industry/Entity Type

e sports/formula one

Colors
0054AA
0677BA
7BADD7
CADEEF
E8F1F8

Requirements
Must have
• Read product description please
Should not have
• Ignoring product description!

```html
<!DOCTYPE html>
<html lang="en">
<head>
<meta charset="utf-8">
<title>Volta Racing League – New Season</title>
<link href="https://fonts.googleapis.com/css2?family=Bungee&family=Poppins:ital,wght@0,800;1,800;1,900&display=swap" rel="stylesheet">
<style>
  :root {
    --navy-deep: #0d0a5e;
    --navy: #1b1580;
    --navy-soft: #3b3a9c;
    --ink: #0a0b4a;
    --violet: #5a12e6;
    --magenta: #e21be0;
    --cyan: #00c3ff;
    --ice: #e4f6ff;
    --gold: #ffc800;
    --white: #ffffff;
  }
  * { margin: 0; padding: 0; box-sizing: border-box; }
  html, body { width: 926px; height: 1200px; overflow: hidden; background: var(--navy-deep); }
  .flyer {
    position: relative;
    width: 926px;
    height: 1200px;
    overflow: hidden;
    font-family: "Poppins", sans-serif;
    color: var(--white);
    background: linear-gradient(180deg, var(--navy-deep) 0%, var(--navy) 45%, var(--navy-soft) 100%);
  }
  .speed-streaks {
    position: absolute; left: 0; top: 60px; width: 560px; height: 360px;
    background: linear-gradient(90deg, rgba(90,18,230,0.85) 0%, rgba(226,27,224,0.45) 30%, rgba(40,30,200,0.2) 70%, transparent 100%);
    filter: blur(6px);
  }
  .flag-area { position: absolute; left: 330px; top: 0; width: 596px; height: 460px; }
  .car-area { position: absolute; left: 0; top: 631px; width: 824px; height: 569px; }
  .badge-mark {
    position: absolute; left: 383px; top: 38px; width: 160px; height: 160px;
    border-radius: 50%; background: var(--ink);
    display: flex; align-items: center; justify-content: center;
    font-family: "Bungee", sans-serif; font-size: 92px; color: var(--white); line-height: 1;
  }
  .title {
    position: absolute; left: 0; width: 926px; top: 196px;
    text-align: center; font-family: "Bungee", sans-serif;
    font-size: 178px; line-height: 1; color: var(--ice); letter-spacing: -2px;
  }
  .rule { position: absolute; height: 3px; background: var(--white); }
  .rule--top { left: 491px; width: 363px; top: 460px; }
  .rule--bottom { left: 272px; width: 359px; top: 553px; }
  .subtitle {
    position: absolute; left: 93px; top: 470px;
    font-style: italic; font-weight: 900; font-size: 64px; line-height: 1.1; letter-spacing: -1px;
  }
  .subtitle .racing { color: var(--cyan); }
  .subtitle .league { color: var(--gold); }
  .slashes { position: absolute; left: 700px; top: 481px; }
  .tagline {
    position: absolute; left: 0; width: 926px; top: 588px; text-align: center;
    font-style: italic; font-weight: 900; font-size: 38px; line-height: 1.1;
  }
  .chip {
    position: absolute; display: flex; align-items: center; justify-content: center;
    font-style: italic; font-weight: 900; color: var(--ink); line-height: 1; letter-spacing: -3px;
  }
  .chip svg { position: absolute; inset: 0; width: 100%; height: 100%; }
  .chip span { position: relative; }
  .chip--new { left: 228px; top: 686px; width: 214px; height: 63px; font-size: 66px; }
  .chip--count { left: 154px; top: 777px; width: 225px; height: 90px; font-size: 100px; }
  .chip--clean { left: 99px; top: 892px; width: 192px; height: 63px; font-size: 52px; }
  .line {
    position: absolute; font-style: italic; font-weight: 900; line-height: 1; white-space: nowrap; letter-spacing: -0.5px;
  }
  .line--white { color: var(--white); }
  .line--cyan { color: var(--cyan); }
  .line--gold { color: var(--gold); }
  .invite {
    position: absolute; left: 228px; top: 994px; width: 469px; height: 49px;
    background: var(--cyan); color: var(--white);
    font-style: italic; font-weight: 800; font-size: 31px; line-height: 49px; text-align: center;
  }
  .schedule {
    position: absolute; left: 0; width: 926px; top: 1050px; text-align: center;
    font-style: italic; font-weight: 800; font-size: 31px; line-height: 38px;
  }
</style>
</head>
<body>
<main class="flyer">
  <div class="speed-streaks"></div>

  <svg class="flag-area" role="img" aria-label="Waving chequered racing flag" viewBox="0 0 596 460" preserveAspectRatio="none">
    <defs>
      <linearGradient id="flagTone" x1="0" y1="0" x2="1" y2="1">
        <stop offset="0" stop-color="#8f86d9" stop-opacity="0.55"/>
        <stop offset="0.5" stop-color="#c9c4ee" stop-opacity="0.55"/>
        <stop offset="1" stop-color="#6f68c4" stop-opacity="0.5"/>
      </linearGradient>
    </defs>
    <path d="M20 120 C160 40 330 30 470 0 L596 0 L596 380 C470 360 320 420 160 460 L0 460 Z" fill="url(#flagTone)"/>
  </svg>

  <svg class="car-area" role="img" aria-label="Formula one race car speeding along the track" viewBox="0 0 824 569" preserveAspectRatio="none">
    <defs>
      <radialGradient id="carTone" cx="0.4" cy="0.75" r="0.7">
        <stop offset="0" stop-color="#2a2560" stop-opacity="0.85"/>
        <stop offset="0.6" stop-color="#4a4a9e" stop-opacity="0.45"/>
        <stop offset="1" stop-color="#3b3a9c" stop-opacity="0"/>
      </radialGradient>
    </defs>
    <rect width="824" height="569" fill="url(#carTone)"/>
  </svg>

  <div class="badge-mark" aria-label="Volta">V</div>

  <h1 class="title">VOLTA</h1>

  <div class="rule rule--top"></div>
  <h2 class="subtitle"><span class="racing">RACING</span> <span class="league">LEAGUE</span></h2>
  <svg class="slashes" width="124" height="55" viewBox="0 0 124 55" aria-hidden="true">
    <polygon points="16,0 36,0 20,55 0,55" fill="var(--cyan)"/>
    <polygon points="48,0 68,0 52,55 32,55" fill="var(--cyan)"/>
    <polygon points="80,0 100,0 84,55 64,55" fill="var(--violet)"/>
    <polygon points="104,0 124,0 108,55 88,55" fill="var(--violet)"/>
  </svg>
  <div class="rule rule--bottom"></div>

  <p class="tagline">RUNNING FOR ITS 4TH YEAR</p>

  <div class="chip chip--new">
    <svg viewBox="0 0 214 63" preserveAspectRatio="none" aria-hidden="true"><polygon points="34,0 214,0 180,63 0,63" fill="var(--gold)"/></svg>
    <span>NEW</span>
  </div>
  <p class="line line--white" style="left:458px; top:684px; font-size:33px;">SEASON</p>
  <p class="line line--cyan" style="left:430px; top:714px; font-size:36px;">JUST STARTING</p>

  <div class="chip chip--count">
    <svg viewBox="0 0 225 90" preserveAspectRatio="none" aria-hidden="true"><polygon points="48,0 225,0 177,90 0,90" fill="var(--gold)"/></svg>
    <span>03</span>
  </div>
  <p class="line line--white" style="left:395px; top:774px; font-size:32px;">DEVISIONS CURRENTY</p>
  <p class="line line--white" style="left:376px; top:804px; font-size:32px;">AND LOOKING TO KEEP</p>
  <p class="line line--cyan" style="left:349px; top:832px; font-size:45px;">GROWING</p>

  <div class="chip chip--clean">
    <svg viewBox="0 0 192 63" preserveAspectRatio="none" aria-hidden="true"><polygon points="32,0 192,0 160,63 0,63" fill="var(--white)"/></svg>
    <span>CLEAN</span>
  </div>
  <p class="line line--white" style="left:316px; top:894px; font-size:30px;">VERY POPULAR AND COMPETITIVE</p>
  <p class="line line--gold" style="left:288px; top:922px; font-size:45px;">ONLINE RACING LEAGE</p>

  <p class="invite">Why not join with a friend?</p>
  <p class="schedule">
    Race times, Mondays, Tuesdays and Wednesdays<br>
    each at 8pm UK TIME<br>
    Message below for any questions
  </p>
</main>
</body>
</html>
```